Adult Job Portal needs a Web Design

We need a web design for a landing and search page for an ADULT-JOB-portal.

The structure of landing page can be taken from tumblewithpals.com.

The structure of job search page can be taken from: http://www.vacancyquarrel.co.uk/

Users should be able to recognize that is a SEX-INDUSTRY job portal.

The project name can not be published for ... some reasons.
Updates

Hi, Pinnlers.

Please note: the project was upgraded to "Guaranteed"
Thanks in advance for great work.
BR. M.

Hi ArtPinnlers,
please find attached the landing page wireframe.
It should make it easier for you to know what is expected.
Thanks in advance, guys!

Target Market(s)

women 18 to 30 years old

Industry/Entity Type

Adult

Requirements
Must have
• We expect to get design for the following pages:
- Landing page
- Add profile (name, description, photos, skills, preferable location)
- Job search with filters (example http://www.vacancyquarrel.co.uk/jobs)
- Companies list (example http://www.vacancyquarrel.co.uk/companies-in-oxfordshire)
- Company page (example http://www.vacancyquarrel.co.uk/company/velquin)
Should not have
• pornography, violence

```html
<!DOCTYPE html>
<html lang="en">
<head>
<meta charset="utf-8">
<title>Noctelle – Jobs for Girls and Clubs</title>
<link rel="stylesheet" href="https://fonts.googleapis.com/css2?family=Open+Sans:wght@400;600&family=Raleway:wght@300&family=Playfair+Display:wght@700&display=swap">
<style>
  :root {
    --red: #c4080e;
    --red-light: #d8262a;
    --black: #000000;
    --ink: #1d1d1d;
    --white: #ffffff;
    --panel: #ffffff;
    --field: #1a1414;
    --field-text: #a9a3a0;
    --tab-frame: #2b2120;
    --icon-grey: #9a9a9a;
    --wall: #7e2a2c;
    --wall-deep: #5e1c1f;
    --chair: #dcb890;
    --chair-rose: #c98a6c;
    --wood: #5a2410;
    --floor: #b47c4c;
    --figure: #24130f;
    --skin: #c8906e;
  }
  * { box-sizing: border-box; margin: 0; padding: 0; }
  html, body { width: 1115px; height: 1200px; overflow: hidden; background: var(--black); }
  body { position: relative; font-family: "Open Sans", Arial, sans-serif; color: var(--ink); }

  .hero { position: absolute; left: 0; top: 0; width: 1115px; height: 597px; overflow: hidden; }
  .hero-photo {
    position: absolute; inset: 0;
    background:
      radial-gradient(ellipse 150px 210px at 320px 200px, rgba(36,19,15,0.95) 0%, rgba(36,19,15,0) 100%),
      radial-gradient(ellipse 230px 230px at 330px 430px, var(--figure) 0%, rgba(36,19,15,0.85) 45%, rgba(36,19,15,0) 100%),
      radial-gradient(ellipse 170px 70px at 560px 430px, var(--skin) 0%, rgba(200,144,110,0) 100%),
      radial-gradient(ellipse 120px 40px at 420px 540px, var(--skin) 0%, rgba(200,144,110,0) 100%),
      radial-gradient(ellipse 110px 220px at 1060px 330px, var(--wood) 0%, rgba(90,36,16,0) 100%),
      radial-gradient(ellipse 330px 280px at 720px 250px, var(--chair) 0%, var(--chair-rose) 55%, rgba(201,138,108,0) 100%),
      linear-gradient(180deg, rgba(180,124,76,0) 86%, var(--floor) 93%, #8a5a34 100%),
      linear-gradient(100deg, var(--wall-deep) 0%, var(--wall) 30%, #8c3234 70%, var(--wall-deep) 100%);
  }

  .brand { position: absolute; left: 50px; top: 18px; display: flex; align-items: center; gap: 14px; }
  .brand-mark {
    width: 153px; height: 153px; border-radius: 50%;
    background: var(--red); border: 10px solid var(--black);
  }
  .brand-name {
    font-weight: 600; font-size: 22px; color: var(--white); letter-spacing: 2px; text-transform: uppercase;
  }

  .hero-intro {
    position: absolute; left: 60px; top: 183px;
    font-size: 16px; line-height: 18.5px; color: var(--white); white-space: nowrap;
  }
  .signup { position: absolute; left: 59px; top: 274px; display: flex; gap: 5px; }
  .signup-email {
    width: 298px; height: 47px; background: var(--field);
    color: var(--field-text); font-size: 16px; padding: 13px 17px;
  }
  .signup-button {
    width: 125px; height: 47px; background: var(--red); color: var(--white);
    font-size: 16px; display: flex; align-items: center; justify-content: center;
  }

  .audience-nav { position: absolute; top: 18px; left: 641px; display: flex; gap: 11px; }
  .audience-tab {
    width: 224px; height: 47px; background: var(--tab-frame); border-radius: 5px; padding: 7px 14px;
  }
  .audience-tab span {
    display: flex; align-items: center; justify-content: center; height: 100%;
    background: var(--red); border-radius: 4px; color: var(--white);
    font-family: "Playfair Display", Georgia, serif; font-weight: 700; font-size: 19px;
  }

  .phone {
    position: absolute; left: 746px; top: 83px; width: 236px; height: 501px;
    background: linear-gradient(90deg, #060608 0%, #16171a 50%, #060608 100%);
    border: 3px solid #5a5c62; border-radius: 36px;
  }
  .phone-speaker {
    position: absolute; left: 97px; top: 28px; width: 38px; height: 5px; border-radius: 3px; background: #3a3a3e;
  }
  .phone-home {
    position: absolute; left: 95px; top: 440px; width: 44px; height: 44px;
    border-radius: 50%; border: 2px solid #46464a;
    background: radial-gradient(circle at 50% 40%, #3a3a3e 0%, #121214 70%);
  }
  .phone-screen {
    position: absolute; left: 13px; top: 68px; width: 204px; height: 362px; overflow: hidden;
    background:
      radial-gradient(ellipse 90px 150px at 70px 250px, #1e110e 0%, rgba(30,17,14,0) 100%),
      radial-gradient(ellipse 70px 120px at 180px 120px, #d3ae88 0%, rgba(211,174,136,0) 100%),
      radial-gradient(ellipse 80px 30px at 130px 300px, #b98464 0%, rgba(185,132,100,0) 100%),
      linear-gradient(160deg, #5a2a26 0%, #3b2220 45%, #4a2c24 100%);
  }
  .phone-status { height: 12px; background: #1a1a1a; }
  .phone-nav {
    display: flex; justify-content: space-between; align-items: center;
    height: 34px; padding: 0 10px; background: rgba(0,0,0,0.78);
    font-family: "Playfair Display", Georgia, serif; font-weight: 700; font-size: 10px; color: var(--white);
  }
  .phone-nav i { width: 28px; height: 28px; border-radius: 50%; background: var(--red); border: 3px solid var(--black); }
  .phone-intro { margin: 10px 14px 0; font-size: 11.6px; line-height: 15px; color: var(--white); }
  .phone-signup { display: flex; gap: 8px; margin: 8px 12px 0; }
  .phone-signup .signup-email { width: 104px; height: 23px; font-size: 9.5px; padding: 5px 8px; }
  .phone-signup .signup-button { width: 68px; height: 23px; font-size: 9.5px; }

  .steps {
    position: absolute; left: 5px; top: 608px; width: 1105px; height: 507px;
    background: var(--panel); border-radius: 8px;
  }
  .step {
    position: absolute; top: 75px; width: 337px; height: 381px;
    border: 3px solid var(--black); border-radius: 12px; padding: 0 16px;
  }
  .step:nth-child(1) { left: 14px; }
  .step:nth-child(2) { left: 384px; }
  .step:nth-child(3) { left: 753px; }
  .step-badge {
    position: absolute; left: 107px; top: -65px; width: 116px; height: 116px;
    border-radius: 50%; border: 10px solid var(--black);
    background: radial-gradient(circle at 50% 55%, #e04a4c 0%, var(--red-light) 30%, var(--red) 70%);
  }
  .step-title {
    margin-top: 62px; text-align: center;
    font-family: "Raleway", Arial, sans-serif; font-weight: 300; font-size: 36px;
    color: var(--ink); letter-spacing: 0.3px; line-height: 42px;
  }
  .step-text { margin-top: 23px; font-size: 13.3px; line-height: 16.5px; color: var(--ink); white-space: nowrap; }
  .step-text + .step-text { margin-top: 16.5px; }

  .site-footer {
    position: absolute; left: 0; top: 1115px; width: 1115px; height: 85px;
    display: flex; justify-content: center; align-items: center; gap: 18px;
  }
  .social-link {
    display: flex; align-items: center; gap: 6px;
    color: var(--icon-grey); font-size: 11px; text-decoration: none;
  }
  .social-link i { width: 30px; height: 30px; border-radius: 50%; background: var(--icon-grey); }
</style>
</head>
<body>
  <header class="hero">
    <div class="hero-photo" role="img" aria-label="Photo of a young woman in dark clothing seated before a floral armchair against a red patterned wall"></div>

    <div class="brand">
      <div class="brand-mark" aria-hidden="true"></div>
      <span class="brand-name">Noctelle</span>
    </div>

    <nav class="audience-nav">
      <a class="audience-tab"><span>FOR GIRLS</span></a>
      <a class="audience-tab"><span>FOR CLUBS</span></a>
    </nav>

    <p class="hero-intro">Lorem ipsum dolor sit amet, consectetur adipisicing elit, sed do eiusmod<br>tempor incididunt ut labore et dolore magna aliqua. Ut enim ad minim<br>veniam, quis nostrud exercitation ullamco laboris nisi ut aliquip ex ea<br>commodo consequat.</p>

    <form class="signup">
      <div class="signup-email">enter email</div>
      <div class="signup-button">subscribe</div>
    </form>

    <div class="phone">
      <div class="phone-speaker"></div>
      <div class="phone-screen" role="img" aria-label="Mobile version of the landing page over the hero photo">
        <div class="phone-status"></div>
        <div class="phone-nav"><span>FOR GIRLS</span><i></i><span>FOR CLUBS</span></div>
        <p class="phone-intro">Lorem ipsum dolor sit amet, consectetur adipisicing elit, sed do eiusmod tempor incididunt ut labore et dolore magna aliqua.</p>
        <div class="phone-signup">
          <div class="signup-email">enter email</div>
          <div class="signup-button">subscribe</div>
        </div>
      </div>
      <div class="phone-home"></div>
    </div>
  </header>

  <main class="steps">
    <section class="step">
      <div class="step-badge" role="img" aria-label="Silhouette of a kneeling woman"></div>
      <h2 class="step-title">FIND</h2>
      <p class="step-text">Lorem ipsum dolor sit amet, consectetur<br>adipisicing elit, sed do eiusmod tempor<br>incididunt ut labore et dolore magna aliqua.<br>Ut enim ad minim veniam, quis nostrud<br>exercitation ullamco laboris nisi ut aliquip ex<br>ea commodo consequat. Duis aute irure dolor<br>in reprehenderit in voluptate velit esse cillum<br>dolore eu fugiat nulla pariatur.</p>
      <p class="step-text">Excepteur sint occaecat cupidatat non<br>proident, sunt in culpa qui officia deserunt<br>mollit anim id est laborum.</p>
    </section>
    <section class="step">
      <div class="step-badge" role="img" aria-label="Silhouette of a crouching woman"></div>
      <h2 class="step-title">APPLY</h2>
      <p class="step-text">Lorem ipsum dolor sit amet, consectetur<br>adipisicing elit, sed do eiusmod tempor<br>incididunt ut labore et dolore magna aliqua.<br>Ut enim ad minim veniam, quis nostrud<br>exercitation ullamco laboris nisi ut aliquip ex<br>ea commodo consequat. Duis aute irure dolor<br>in reprehenderit in voluptate velit esse cillum<br>dolore eu fugiat nulla pariatur.</p>
      <p class="step-text">Excepteur sint occaecat cupidatat non<br>proident, sunt in culpa qui officia deserunt<br>mollit anim id est laborum.</p>
    </section>
    <section class="step">
      <div class="step-badge" role="img" aria-label="Silhouette of a reclining woman"></div>
      <h2 class="step-title">MOVE</h2>
      <p class="step-text">Lorem ipsum dolor sit amet, consectetur<br>adipisicing elit, sed do eiusmod tempor<br>incididunt ut labore et dolore magna aliqua.<br>Ut enim ad minim veniam, quis nostrud<br>exercitation ullamco laboris nisi ut aliquip ex<br>ea commodo consequat. Duis aute irure dolor<br>in reprehenderit in voluptate velit esse cillum<br>dolore eu fugiat nulla pariatur.</p>
      <p class="step-text">Excepteur sint occaecat cupidatat non<br>proident, sunt in culpa qui officia deserunt<br>mollit anim id est laborum.</p>
    </section>
  </main>

  <footer class="site-footer">
    <a class="social-link"><i></i>Murmur</a>
    <a class="social-link"><i></i>Kinfold</a>
    <a class="social-link"><i></i>Circlet</a>
  </footer>
</body>
</html>
```